Professional Business Card for Luxury Hotel & Resort Development Firm. Advisory firm

Project Overview: We are a specialized advisory firm focused on Hotel & Resort Development. Our clients are high-net-worth investors and major hospitality brands.

Design Requirements:

Style: Minimalist, sophisticated, and trustworthy. We want to avoid looking too "corporate" or "dry"—it should feel premium.

Key Elements: Please incorporate our logo [もしロゴがあれば] and emphasize a clean layout with plenty of white space.

Color Palette: We prefer Grey and White or Black and White to evoke a sense of luxury and stability.

Typography: Professional garamond, or sans-serif or elegant serif fonts

Goal: The card should feel substantial and high-end when handed to a client, reflecting our expertise in multi-million dollar developments.
Updates

I am currently on a business trip for field research and have limited access to my desktop. Additionally, I have just provided detailed technical feedback to a designer and am waiting for their refined proposals. To ensure the final logo meets the high standards of my new advisory firm, I would like to extend the deadline by 7 days. Thank you for your support.

Target Market(s)

High-net-worth investors, luxury hospitality brands, and real estate developers.

Contact Information for Business Card

Firm Name: Larkfield Counsel Partners, My Name: Kenji Morisawa, Title: Founder, Address 5-7-4 Kitakawabe Asahi Yokohama Japan 241-0815, email address: kmorisawa@larkfieldcp.com, Tel: +81 80-4821-3357. Front Site (Primary): Japanese translation of the back side, Please use a clean Japanese font (like Mincho) that complements the Garmond on the English side Back side: English. Note for Japanese text: since the frond side is the main fae, please ensure the layout is clean and professional. Please use a high-quality Mincho ( Serif-style) font for Japanese to mach the Garmond used on the English side. Text for Front side (Japanese) Larkfield Counsel Partners, 役職:代表、森沢健二、241-0815 横浜市旭区北川辺5-7-4. Name of the firm can stay in English.

Font styles to use
Other font styles liked:
• Font Preference: Please use Garamond for all text to maintain a consistent, elegant, and classic professional look.

Requirements
Must have
• Professional and clean layout, high-end feel.
Nice to have
• Minimalist design with subtle luxury accents.

```html
<!DOCTYPE html>
<html lang="ja">
<head>
<meta charset="utf-8">
<title>Larkfield Counsel Partners — Business Card Front</title>
<link rel="stylesheet" href="https://fonts.googleapis.com/css2?family=EB+Garamond:wght@400;600&family=Shippori+Mincho:wght@400;500&display=swap">
<style>
  :root {
    --backdrop: #ececec;
    --card: #ffffff;
    --ink: #3a3a3a;
    --ink-soft: #4a4a4a;
  }
  * { margin: 0; padding: 0; box-sizing: border-box; }
  html, body {
    width: 1200px;
    height: 1200px;
    overflow: hidden;
    background: var(--backdrop);
  }
  .stage {
    width: 1200px;
    height: 1200px;
    display: flex;
    align-items: center;
    justify-content: center;
  }
  .card {
    position: relative;
    width: 1040px;
    height: 597px;
    background: var(--card);
    border-radius: 21px;
    color: var(--ink);
    text-align: center;
  }
  .firm-name {
    position: absolute;
    top: 82px;
    left: 0;
    right: 0;
    font-family: "EB Garamond", Garamond, serif;
    font-weight: 600;
    font-size: 30px;
    letter-spacing: 0.2px;
  }
  .person {
    position: absolute;
    top: 246px;
    left: 0;
    right: 0;
    font-family: "Shippori Mincho", "EB Garamond", serif;
  }
  .person-title {
    font-size: 20px;
    line-height: 1.2;
    color: var(--ink-soft);
  }
  .person-name {
    margin-top: 4px;
    font-size: 42px;
    font-weight: 500;
    line-height: 1.2;
    letter-spacing: 1px;
  }
  .address {
    position: absolute;
    top: 458px;
    left: 0;
    right: 0;
    font-family: "Shippori Mincho", "EB Garamond", serif;
    font-size: 20px;
    line-height: 28px;
    color: var(--ink-soft);
  }
  .address .latin {
    font-family: "EB Garamond", Garamond, serif;
    font-size: 21px;
    letter-spacing: -0.3px;
  }
</style>
</head>
<body>
  <main class="stage">
    <section class="card" aria-label="名刺 表面">
      <h1 class="firm-name">Larkfield Counsel Partners</h1>
      <div class="person">
        <p class="person-title">代表</p>
        <p class="person-name">森沢 健二</p>
      </div>
      <address class="address">
        <p>〒<span class="latin">241-0815</span></p>
        <p>横浜市旭区北川辺<span class="latin">5-7-4</span></p>
      </address>
    </section>
  </main>
</body>
</html>
```